Poster: Meditation course

We would like a simple poster to advertise a 10-day meditation course. We would like something very simple and minimal, nothing fancy. We will be putting this poster up around our local area and leaving it on cafe tables etc. We will also be sending it around digitally.
The poster should include the words below. (Please note that we may want to change these words further along in the process.) And in terms of imagery, something like a lotus flower could work well. (Please see the attached lotus flower and lily image in our newsletters, although it doesn't need to be that old school.) The size can be US Letter size / Europe A4. Please include the attached QR code, and please note that for the digital version we would like hyperlinks for the webpage and email. Many thanks!
Text for the poster:
Meditation produces a calm mind
10-day residential meditation course
Half Moon Bay, California
7-17th June 2024
Vipassana meditation in the Theravada Buddhism tradition as taught by Teacher Lo Denmar and Sister Orvelina
To apply: https://www.quietridgestillness.example/
For more information contact: info@quietridgestillness.example
Target Market(s)
Primarily university students. Also other people in California
Look and feel

```html
<!DOCTYPE html>
<html lang="en">
<head>
<meta charset="utf-8">
<title>Meditation Course Poster</title>
<link href="https://fonts.googleapis.com/css2?family=Playfair+Display:wght@400;500&family=Josefin+Sans:wght@400;600&display=swap" rel="stylesheet">
<style>
  :root {
    --backdrop: #7f7f7f;
    --poster-black: #020505;
    --ink: #ffffff;
    --teal-deep: #0b3a34;
    --teal-glow: #1f7a6d;
    --lotus-white: #f4eef2;
    --lotus-pink: #d889b6;
  }
  * { margin: 0; padding: 0; box-sizing: border-box; }
  html, body { width: 1200px; height: 1070px; overflow: hidden; background: var(--backdrop); }
  .poster {
    position: absolute; left: 243px; top: 30px; width: 714px; height: 1010px;
    background: var(--poster-black); color: var(--ink); overflow: hidden;
  }
  .poster > * { position: absolute; }
  .centered { left: 0; width: 100%; text-align: center; }
  .lotus-artwork {
    left: 0; top: 232px; width: 100%; height: 560px;
    background:
      radial-gradient(ellipse 150px 160px at 50% 52%, var(--lotus-white) 0%, rgba(230,190,215,0.85) 45%, rgba(216,137,182,0) 75%),
      radial-gradient(ellipse 330px 260px at 50% 55%, var(--teal-glow) 0%, var(--teal-deep) 50%, rgba(2,5,5,0) 100%);
  }
  .title {
    top: 64px; font-family: "Playfair Display", serif; font-weight: 400;
    font-size: 82px; letter-spacing: 0.075em; line-height: 1; padding-left: 0.075em;
  }
  .tagline {
    top: 155px; font-family: "Josefin Sans", sans-serif; font-weight: 600;
    font-size: 17px; letter-spacing: 0.62em; padding-left: 0.62em;
  }
  .rule { height: 1.5px; background: var(--ink); }
  .rule--tagline { top: 190px; left: 186px; width: 345px; }
  .course-type {
    top: 213px; font-family: "Josefin Sans", sans-serif; font-weight: 600;
    font-size: 12px; letter-spacing: 0.58em; padding-left: 0.58em;
  }
  .rule--date-top { top: 755px; left: 156px; width: 402px; }
  .rule--date-bottom { top: 891px; left: 156px; width: 402px; top: 891px; }
  .dates {
    top: 760px; font-family: "Playfair Display", serif; font-weight: 500;
    font-size: 48px; line-height: 1.2;
  }
  .dates sup { font-size: 22px; vertical-align: 20px; }
  .location {
    top: 828px; font-family: "Josefin Sans", sans-serif; font-weight: 600;
    font-size: 13px; letter-spacing: 0.45em; padding-left: 0.45em;
  }
  .tradition {
    top: 860px; font-family: "Josefin Sans", sans-serif; font-weight: 600;
    font-size: 12px; letter-spacing: 0.2em; line-height: 20px;
  }
  .teachers {
    top: 902px; font-family: "Playfair Display", serif; font-weight: 400;
    font-size: 22px; text-transform: uppercase; letter-spacing: 0.01em; word-spacing: 2px;
  }
  .contact { top: 960px; display: flex; align-items: center; }
  .contact--web { left: 37px; }
  .contact--mail { left: 408px; }
  .contact-icon {
    width: 30px; height: 30px; border-radius: 50%; background: var(--ink);
    display: flex; align-items: center; justify-content: center; flex: none;
  }
  .contact-link {
    margin-left: 3px; height: 22px; padding: 0 6px; border: 1px solid var(--ink);
    border-left: none; display: flex; align-items: center;
    font-family: "Josefin Sans", sans-serif; font-size: 9px; font-weight: 400;
    color: var(--ink); text-decoration: none; text-transform: uppercase; letter-spacing: 0.01em;
  }
  .contact--web .contact-link { width: 239px; }
  .contact--mail .contact-link { width: 244px; }
</style>
</head>
<body>
<main class="poster">
  <div class="lotus-artwork" role="img" aria-label="Photograph of a white and pink lotus flower glowing among dark teal lotus leaves"></div>

  <h1 class="title centered">MEDITATION</h1>
  <p class="tagline centered">PRODUCES A CALM MIND</p>
  <div class="rule rule--tagline"></div>
  <p class="course-type centered">10-DAY RESIDENTIAL MEDITATION COURSE</p>

  <div class="rule rule--date-top"></div>
  <p class="dates centered">7–17<sup>TH</sup> JUNE 2024</p>
  <div class="rule" style="top:820px;left:156px;width:402px;"></div>
  <p class="location centered">HALF MOON BAY, CALIFORNIA</p>
  <p class="tradition centered" style="top:860px;">VIPASSANA MEDITATION IN THE THERAVADA BUDDHISM TRADITION<br>AS TAUGHT BY</p>
  <p class="teachers centered">Teacher Lo Denmar &nbsp;&amp;&nbsp; Sister Orvelina</p>

  <div class="contact contact--web">
    <span class="contact-icon">
      <svg width="18" height="18" viewBox="0 0 18 18" fill="none" stroke="#020505" stroke-width="1.3">
        <rect x="4" y="2" width="10" height="14" rx="1"/>
        <path d="M6.5 6h5M6.5 9h5M6.5 12h3"/>
        <circle cx="4" cy="4" r="2.6" fill="#fff"/>
        <path d="M2.8 4l0.9 0.9 1.6-1.7"/>
      </svg>
    </span>
    <a class="contact-link" href="https://www.quietridgestillness.example/">www.quietridgestillness.example</a>
  </div>

  <div class="contact contact--mail">
    <span class="contact-icon">
      <svg width="18" height="14" viewBox="0 0 18 14" fill="none" stroke="#020505" stroke-width="1.4">
        <rect x="1" y="1" width="16" height="12"/>
        <path d="M1 1l8 6.5L17 1M1 13l6-5.5M17 13l-6-5.5"/>
      </svg>
    </span>
    <a class="contact-link" href="mailto:info@quietridgestillness.example">info@quietridgestillness.example</a>
  </div>
</main>
</body>
</html>
```